Pine Hollow toothpaste tube design

Design a Pine Hollow tube design for our all natural toothpaste. The toothpaste is 100% natural with a smooth marshmallow consistency. It's unique because it's not pastelike at all. The all natural flavors make the toothpaste taste great. The toothpaste is smooth yet still leaves your mouth feeling squeaky clean. We want to market this as an all natural family toothpaste.

The flavor is Mint. (possibly called "Koda Fern")

We have included our logo (eps & jpg), information that goes on the back of the tube, and the artwork template from the tube supplier for the 4.2oz tube.

We like a vintage earthy retro look and feel but we are not limited to this.

The tubes stand upright as shown in the picture of File 4.
Updates

The finished artwork must include anĀ adobe illustratorĀ file.

Project Deadline Extended

I would like to thank all of the designers for their work on this project. We had a difficult time making a decision since all of the designs were very close to what we expected.

Sincerely,

Rolf

Target Market(s)

The target market is families that desire an all natural toothpaste. We will be stressing the 100% natural and great taste.

Requirements
Must have
• Three colors maximum due to tube manufacture restrictions.

Must have "100% natural" and "fluoride free" on front of tube. A reference to the great taste or flavor is also important.

Must say 4.2 oz on the front of the tube, centered, at the bottom.
Nice to have
• Fun, colorful packaging that will stand out. Go to your local store and stand in front of the tootpaste shelves, give us something different!
Should not have
• We do not want a lot of red or blue because these are predominate colors already in use on toothpaste tubes and boxes.

```html
<!DOCTYPE html>
<html lang="en">
<head>
<meta charset="utf-8">
<title>Pine Hollow – Koda Fern toothpaste tube label</title>
<link rel="stylesheet" href="https://fonts.googleapis.com/css2?family=Nunito:wght@700;800;900&family=Caveat+Brush&display=swap">
<style>
  :root{
    --green:#2f8f3f;
    --green-deep:#237532;
    --green-soft:#4aa457;
    --white:#ffffff;
    --stage:#f2f3ef;
    --edge:#dfe3dc;
  }
  *{box-sizing:border-box;margin:0;padding:0}
  html,body{width:1200px;height:898px;overflow:hidden;background:var(--stage)}
  body{position:relative;font-family:"Nunito",Arial,sans-serif}

  .label{
    position:absolute;top:64px;width:340px;height:770px;
    background:var(--white);border:1px solid var(--edge);overflow:hidden;
  }
  .label--front{left:205px}
  .label--back{left:655px}

  .green-field{
    position:absolute;left:0;right:0;bottom:0;top:330px;background:var(--green);
  }
  .grass-edge{
    position:absolute;left:0;right:0;top:292px;height:46px;
    background:linear-gradient(to bottom,rgba(47,143,63,0) 0%,rgba(47,143,63,.55) 55%,var(--green) 100%);
  }

  .brand{
    position:absolute;left:0;right:0;display:flex;align-items:center;justify-content:center;gap:10px;
    color:var(--green);font-weight:900;
  }
  .brand__dot{width:16px;height:16px;border-radius:50%;background:var(--green)}
  .label--front .brand{top:110px;font-size:46px;letter-spacing:-1px}
  .label--back .brand{top:44px;font-size:30px;letter-spacing:-.5px}
  .label--back .brand__dot{width:11px;height:11px}

  .flavour{
    position:absolute;left:0;right:0;top:360px;text-align:center;
    font-family:"Caveat Brush",cursive;color:var(--white);font-size:50px;line-height:1;
  }
  .flavour-rule{position:absolute;left:62px;width:216px;top:420px;height:3px;background:var(--white);opacity:.9;border-radius:2px}

  .leaf-decor{
    position:absolute;left:-40px;top:440px;width:220px;height:220px;border-radius:50% 10% 50% 10%;
    background:radial-gradient(circle at 40% 40%,var(--green-soft),var(--green) 70%);opacity:.7;
  }

  .claims{
    position:absolute;left:0;right:0;top:445px;list-style:none;text-align:center;
    color:var(--white);font-weight:800;font-size:19px;line-height:30px;
  }
  .claims li::before{content:"• ";}

  .badge{
    position:absolute;left:190px;top:615px;width:104px;height:104px;border-radius:50%;
    border:3px solid var(--white);
  }
  .badge::after{content:"";position:absolute;inset:8px;border-radius:50%;border:2px solid var(--white)}

  .net-weight{
    position:absolute;left:0;right:0;bottom:22px;text-align:center;color:var(--white);
    font-weight:800;font-size:20px;
  }

  .directions{
    position:absolute;left:34px;right:34px;top:110px;text-align:center;color:var(--green);
    font-weight:800;font-size:14px;line-height:19px;
  }
  .back-copy{
    position:absolute;left:30px;right:30px;top:360px;text-align:center;color:var(--white);
    font-weight:800;font-size:12.5px;line-height:17px;
  }
  .back-copy p+p{margin-top:16px}
</style>
</head>
<body>

<section class="label label--front">
  <div class="brand"><span class="brand__dot"></span>Pine Hollow</div>
  <div class="grass-edge" role="img" aria-label="Grass and plant silhouettes along the top of the green band"></div>
  <div class="green-field"></div>
  <div class="leaf-decor" role="img" aria-label="Large faint mint leaf illustration"></div>
  <div class="flavour">koda fern</div>
  <div class="flavour-rule"></div>
  <ul class="claims">
    <li>100% Natural toothpaste</li>
    <li>Natural flavours</li>
    <li>Flouride free</li>
    <li>Smooth, great taste</li>
    <li>For all the family</li>
  </ul>
  <div class="badge" role="img" aria-label="Round seal"></div>
  <div class="net-weight">4.2oz</div>
</section>

<section class="label label--back">
  <div class="brand"><span class="brand__dot"></span>Pine Hollow</div>
  <p class="directions">Directions:<br>Adults and children 2 years of age and older: Brush teeth thoroughly, preferably after each meal or at least twice a day or as directed by a dentist. Children under 2: consult a dentist.</p>
  <div class="grass-edge" role="img" aria-label="Grass and plant silhouettes along the top of the green band"></div>
  <div class="green-field"></div>
  <div class="back-copy">
    <p>Natural Ingredients: vegetable glycerin, de-ionized water, xylitol, calcium carbonate, USDA organic flavor concentrate, sodium coco-sulfate (derived from coconut oil), and carrageenan (extracted from seaweed).</p>
    <p>No parabens, no gluten, no glycols, no SLS, no TEA, no formaldehyde, no artificial flavors, no artificial dye, no artificial sweetener, no dairy, no sorbitol, no saccharines, no peroxides, and no fluoride!</p>
    <p>Made in USA<br>Distribution &amp; Supply Facility:<br>Pine Hollow LLC<br>218 Alder Ridge Rd<br>Millbrook, OR 97301<br>www.pinehollowcare.com<br>hello@pinehollowcare.com</p>
  </div>
</section>

</body>
</html>
```